New Business Card Design Project VORASTI-Italy

we are VORASTI-Italy
our company in the market for 3 years we are luxury cosmetic company and its about time for a facelift :)
i will like to have elegant luxurious and unique business card
that will give the person that get it a unique, luxurious and elegant impression
I'm VERY OPEN FOR NEW IDEAS , even duo i add a few files of things that i see on line and i like them

i add my logo as well
my website is VORASTI.COM
(if you would like to see the main style that we have)

Target Market(s)

adult that have money :)

Industry/Entity Type

Business

Contact Information for Business Card

Name - Paul Vorasti
Position - CEO and CO Founder
address - 4817 E Larkdale
telephone - 555-384-1962
email - paul@vorasti.com
fax - 555-384-1962
website - VORASTI.COM

Colors
000000
959595
fbee3e
ffffff

Requirements
Must have
• big logo in GOLD color
• elegant look
• impressive
Nice to have
• not must but maybe classy pattern background
• not must but maybe emblem
• maybe clear plastic business card
Should not have
• colors
• images

```html
<!DOCTYPE html>
<html lang="en">
<head>
<meta charset="utf-8">
<title>Paul Vorasti – Business Card</title>
<link rel="stylesheet" href="https://fonts.googleapis.com/css2?family=Marcellus+SC&family=Tinos&display=swap">
<style>
  :root {
    --backdrop: #6f6f6f;
    --card: #2b2b2c;
    --card-edge: #1f1f20;
    --gold: #c9a23a;
    --gold-soft: #a8862c;
    --gold-faint: rgba(201, 162, 58, 0.22);
  }
  * { margin: 0; padding: 0; box-sizing: border-box; }
  html, body {
    width: 1200px;
    height: 736px;
    overflow: hidden;
    background: var(--backdrop);
  }
  .stage {
    position: relative;
    width: 1200px;
    height: 736px;
    display: flex;
    align-items: center;
    justify-content: center;
  }
  .card {
    position: relative;
    width: 1000px;
    height: 572px;
    background: var(--card);
    border: 1px solid var(--card-edge);
    overflow: hidden;
  }
  .card__emblem {
    position: absolute;
    left: -40px;
    top: 60px;
    width: 340px;
    height: 340px;
  }
  .card__identity {
    position: absolute;
    right: 70px;
    top: 70px;
    text-align: left;
    color: var(--gold);
    font-family: "Marcellus SC", serif;
  }
  .card__name {
    font-size: 46px;
    font-weight: 400;
    letter-spacing: 1px;
    line-height: 1.05;
  }
  .card__title {
    font-size: 24px;
    letter-spacing: 1.5px;
    color: var(--gold-soft);
    text-transform: uppercase;
    line-height: 1.2;
  }
  .card__contact {
    position: absolute;
    left: 330px;
    top: 400px;
    width: 560px;
    text-align: center;
    color: var(--gold);
    font-family: "Tinos", serif;
    font-size: 21px;
    line-height: 1.25;
    font-style: normal;
  }
</style>
</head>
<body>
  <main class="stage">
    <article class="card">
      <svg class="card__emblem" viewBox="0 0 340 340" role="img" aria-label="Circular gold line ornament with a geometric zigzag ring">
        <defs>
          <radialGradient id="emblemGlow" cx="50%" cy="50%" r="50%">
            <stop offset="55%" stop-color="#c9a23a" stop-opacity="0.04"/>
            <stop offset="80%" stop-color="#c9a23a" stop-opacity="0.22"/>
            <stop offset="100%" stop-color="#c9a23a" stop-opacity="0.08"/>
          </radialGradient>
        </defs>
        <circle cx="170" cy="170" r="168" fill="url(#emblemGlow)"/>
      </svg>

      <header class="card__identity">
        <h1 class="card__name">Paul Vorasti</h1>
        <p class="card__title">CEO and Co Founder</p>
      </header>

      <address class="card__contact">
        Address - 4817 E Larkdale ; Phone - 555-384-1962<br>
        Email - paul@vorasti.com ; Fax - 555-384-1962<br>
        Website - VORASTI.COM
      </address>
    </article>
  </main>
</body>
</html>
```